Premium Van Wrap Design for Drone Cleaning Business (Dual Branding Concept)

We are looking for a highly creative and experienced graphic designer to develop a visually striking, premium van wrap design for a drone-based cleaning business.
The vehicle will act primarily as a mobile demonstration unit, showcasing cutting-edge drone cleaning solutions across multiple industries including wind turbines, warehouses, building façades, and solar farms.
The design must communicate innovation, efficiency, and industrial capability, while remaining clean, modern, and highly professional.
CORE CHALLENGE (Key Requirement)
This project requires a flexible dual-branding solution.
The van will operate under two brands:
- Primary (Demo Mode): SkyRinseWorks.net (no logo yet)
- Secondary (Commercial Work): The Copper Kestrel
The design must allow branding to be switched using magnetic overlay panels therefore consideration for van panels (Valtoria Carrex T7R2).
This means:
- The base wrap should be visually complete without relying on fixed branding in key areas
- Specific zones must be designed where magnetic panels can be applied seamlessly
- The switch between brands must look intentional and premium, not like an afterthought
Designers must account for this modular branding approach from the outset.
DESIGN OBJECTIVES
The wrap should:
- Look high-end and technologically advanced
- Clearly communicate drone-based cleaning solutions
- Showcase multiple use cases visually:
- Wind turbines
- Industrial warehouses
- Building façades
- Solar panels
- Feel dynamic and eye-catching even at distance
- Avoid clutter while still telling a strong visual story
- Work across all van surfaces (sides, rear, bonnet if applicable)
STYLE DIRECTION
We are aiming for:
- Clean, modern, and bold
- Industrial + tech aesthetic
- Subtle gradients, depth, and motion where appropriate
- Strong visual hierarchy
- Minimal but impactful text
Avoid:
- Overly busy layouts
- Clip-art style graphics
- Low-end “signage” look
Think premium fleet branding rather than standard van graphics.
FUNCTIONAL REQUIREMENTS
- Design must include clearly defined zones for magnetic overlays
- Branding areas should be easy to swap without disrupting the overall design
- Consider how logos, taglines, and contact details will adapt between brands
- Ensure readability at distance and in motion
- Must be print-ready for professional vehicle wrapping
DELIVERABLES
- Full van wrap design (all sides, rear, optional bonnet)
- Layered source files (Adobe Illustrator preferred)
- Print-ready files with correct dimensions and bleed
- Visual mockups (realistic render of van we can supply a 3D Model of van)
- Clear indication of magnetic overlay zones
INFORMATION TO BE PROVIDED
We will supply:
- Logos for The Copper Kestrel - you have free reign over SkyRinseWorks.net
Vehicle dimensions/template (also 3D model of van available on request for renders)
IDEAL DESIGNER
We are looking for someone who:
- Has strong experience in vehicle wrap design
- Demonstrates high-end branding work
- Understands spatial design and large-format layouts
- Can think creatively about modular branding systems

```html
<!DOCTYPE html>
<html lang="en">
<head>
<meta charset="utf-8">
<title>SkyRinseWorks.net – Van Wrap Layout</title>
<link rel="stylesheet" href="https://fonts.googleapis.com/css2?family=Oswald:wght@600;700&family=Roboto+Condensed:wght@500;700&family=Montserrat:wght@700&display=swap">
<style>
  :root {
    --backdrop: #bdbdbd;
    --van-white: #ffffff;
    --glass: #bdbdbd;
    --steel-blue: #6786a6;
    --steel-blue-dark: #4f6c8a;
    --navy: #15253a;
    --stripe-dark: #2a2a2a;
    --sky-light: #d3dbe2;
    --sky-deep: #2d4763;
  }
  html, body {
    margin: 0;
    padding: 0;
    width: 693px;
    height: 1200px;
    overflow: hidden;
    background: var(--backdrop);
  }
  .sheet {
    width: 693px;
    height: 1200px;
    display: flex;
    flex-direction: column;
    justify-content: center;
    gap: 150px;
  }
  .van-layout { display: block; width: 693px; }
  .van-body { fill: var(--van-white); }
  .van-glass { fill: var(--glass); }
  .panel-seam { stroke: var(--glass); stroke-width: 4; }
  .cert-tab { fill: var(--steel-blue); }
  .cert-text {
    font-family: 'Roboto Condensed', sans-serif;
    font-weight: 500;
    font-size: 24px;
    fill: #ffffff;
  }
  .headline {
    font-family: 'Oswald', sans-serif;
    font-weight: 700;
    font-size: 58px;
    fill: var(--navy);
    letter-spacing: -0.5px;
  }
  .contact-band { fill: var(--steel-blue); }
  .contact-rule { fill: var(--steel-blue); }
  .phone {
    font-family: 'Roboto Condensed', sans-serif;
    font-weight: 700;
    font-size: 50px;
    fill: #ffffff;
  }
  .web {
    font-family: 'Oswald', sans-serif;
    font-weight: 600;
    font-size: 36px;
    fill: #ffffff;
  }
  .stripe-blue { fill: var(--steel-blue); }
  .stripe-dark { fill: var(--stripe-dark); }
  .brand-mark { fill: var(--navy); }
  .brand-name {
    font-family: 'Montserrat', sans-serif;
    font-weight: 700;
    font-size: 15px;
    fill: var(--navy);
  }
  .brand-tagline {
    font-family: 'Montserrat', sans-serif;
    font-weight: 700;
    font-size: 6px;
    fill: var(--navy);
  }
</style>
</head>
<body>
<main class="sheet">

  <!-- Driver side (nose left) -->
  <svg class="van-layout" viewBox="100 1400 1260 468" xmlns="http://www.w3.org/2000/svg" aria-label="Driver side wrap layout">
    <defs>
      <linearGradient id="sceneLeft" x1="0" y1="0" x2="1" y2="0">
        <stop offset="0" stop-color="var(--sky-light)"/>
        <stop offset="0.45" stop-color="#8fa2b6"/>
        <stop offset="1" stop-color="var(--sky-deep)"/>
      </linearGradient>
    </defs>
    <path class="van-body" d="M470 1425 L1285 1415 Q1305 1430 1310 1470 L1335 1610 L1312 1780 L1130 1780 Q1100 1742 1045 1742 Q985 1742 958 1780 L958 1862 L300 1862 L292 1800 Q270 1765 225 1765 Q185 1768 165 1775 L135 1740 L160 1690 L118 1685 Q190 1640 272 1610 L285 1560 Q360 1470 470 1425 Z"/>
    <path class="van-body" d="M1120 1812 L1288 1812 L1284 1856 L1124 1856 Z"/>
    <path class="van-glass" d="M300 1600 Q340 1532 420 1527 L476 1530 L462 1640 L292 1676 Z"/>
    <line class="panel-seam" x1="365" y1="1812" x2="955" y2="1812"/>
    <line class="panel-seam" x1="496" y1="1780" x2="496" y2="1812"/>
    <line class="panel-seam" x1="776" y1="1780" x2="776" y2="1812"/>

    <rect class="scene-photo" x="850" y="1503" width="423" height="122" rx="12" fill="url(#sceneLeft)" role="img" aria-label="Photo: cleaning drone spraying a glass office façade"/>

    <path class="cert-tab" d="M527 1497 L660 1497 L672 1525 L527 1525 Z"/>
    <text class="cert-text" x="533" y="1519">C5 CERTIFIED</text>
    <text class="headline" x="524" y="1573">CLEANING</text>
    <text class="headline" x="524" y="1622">DRONE SYSTEM</text>

    <rect class="contact-band" x="524" y="1630" width="747" height="60"/>
    <rect class="contact-rule" x="524" y="1695" width="747" height="4"/>
    <text class="phone" x="540" y="1681">0100 555 0192</text>
    <circle cx="840" cy="1665" r="4" fill="#ffffff"/>
    <text class="web" x="858" y="1676">SkyRinseWorks.net</text>

    <g class="hazard-stripes">
      <path class="stripe-blue" d="M1110 1701 L1135 1701 L1118 1719 L1093 1719 Z"/>
      <path class="stripe-dark" d="M1145 1701 L1170 1701 L1153 1719 L1128 1719 Z"/>
      <path class="stripe-blue" d="M1180 1701 L1205 1701 L1188 1719 L1163 1719 Z"/>
      <path class="stripe-dark" d="M1215 1701 L1240 1701 L1223 1719 L1198 1719 Z"/>
      <path class="stripe-blue" d="M1250 1701 L1270 1701 L1253 1719 L1233 1719 Z"/>
    </g>

    <g class="brand-lockup">
      <circle class="brand-mark" cx="360" cy="1712" r="16"/>
      <text class="brand-name" x="360" y="1752" text-anchor="middle">The Copper Kestrel</text>
      <text class="brand-tagline" x="360" y="1765" text-anchor="middle">ALOFT &amp; UNRIVALLED</text>
    </g>
  </svg>

  <!-- Passenger side (nose right) -->
  <svg class="van-layout" viewBox="100 1935 1260 478" xmlns="http://www.w3.org/2000/svg" aria-label="Passenger side wrap layout">
    <defs>
      <linearGradient id="sceneRight" x1="1" y1="0" x2="0" y2="0">
        <stop offset="0" stop-color="var(--sky-light)"/>
        <stop offset="0.45" stop-color="#8fa2b6"/>
        <stop offset="1" stop-color="var(--sky-deep)"/>
      </linearGradient>
    </defs>
    <g transform="translate(1455 530) scale(-1 1)">
      <path class="van-body" d="M470 1425 L1285 1415 Q1305 1430 1310 1470 L1335 1610 L1312 1780 L1130 1780 Q1100 1742 1045 1742 Q985 1742 958 1780 L958 1862 L300 1862 L292 1800 Q270 1765 225 1765 Q185 1768 165 1775 L135 1740 L160 1690 L118 1685 Q190 1640 272 1610 L285 1560 Q360 1470 470 1425 Z"/>
      <path class="van-body" d="M1120 1812 L1288 1812 L1284 1856 L1124 1856 Z"/>
      <path class="van-glass" d="M300 1600 Q340 1532 420 1527 L476 1530 L462 1640 L292 1676 Z"/>
      <line class="panel-seam" x1="365" y1="1812" x2="955" y2="1812"/>
      <line class="panel-seam" x1="964" y1="1780" x2="964" y2="1812"/>
    </g>

    <rect class="scene-photo" x="172" y="2000" width="430" height="125" rx="12" fill="url(#sceneRight)" role="img" aria-label="Photo: cleaning drone spraying a glass office façade"/>

    <path class="cert-tab" d="M803 2005 L937 2005 L937 2032 L791 2032 Z"/>
    <text class="cert-text" x="931" y="2027" text-anchor="end">C5 CERTIFIED</text>
    <text class="headline" x="937" y="2082" text-anchor="end">CLEANING</text>
    <text class="headline" x="937" y="2131" text-anchor="end">DRONE SYSTEM</text>

    <rect class="contact-band" x="172" y="2128" width="470" height="68"/>
    <rect class="contact-band" x="500" y="2138" width="437" height="58"/>
    <rect class="contact-rule" x="172" y="2200" width="765" height="4"/>
    <text class="phone" x="188" y="2178">0100 555 0192</text>
    <circle cx="500" cy="2162" r="4" fill="#ffffff"/>
    <text class="web" x="528" y="2174">SkyRinseWorks.net</text>

    <g class="hazard-stripes">
      <path class="stripe-blue" d="M172 2206 L197 2206 L215 2224 L190 2224 Z"/>
      <path class="stripe-dark" d="M207 2206 L232 2206 L250 2224 L225 2224 Z"/>
      <path class="stripe-blue" d="M242 2206 L267 2206 L285 2224 L260 2224 Z"/>
      <path class="stripe-dark" d="M277 2206 L302 2206 L320 2224 L295 2224 Z"/>
      <path class="stripe-blue" d="M312 2206 L337 2206 L355 2224 L330 2224 Z"/>
    </g>

    <g class="brand-lockup">
      <circle class="brand-mark" cx="1072" cy="2245" r="16"/>
      <text class="brand-name" x="1072" y="2287" text-anchor="middle">The Copper Kestrel</text>
      <text class="brand-tagline" x="1072" y="2300" text-anchor="middle">ALOFT &amp; UNRIVALLED</text>
    </g>
  </svg>

</main>
</body>
</html>
```